Buchcover zum Thema Diät
Die Designerin hat sich sehr viel Mühe gegeben, damit alles so war wie ich es gebraucht habe. Sie hat auf meine Fragen auch immer schnell geantwortet. Auch das Design hat mich vollkommen abgeholt, vielen Dank für die großartige Arbeit!
Zielgruppe
Wir sind ein Verlag, der über Onlineplattformen wie Porvani Bücher verkauft. Unsere Zielgruppe sind mehrheitlich Frauen zwischen 25 und 55.
Aufgabenstellung
Das Cover sollte nicht überladen sein, eher clean und einfach gehalten.
Buchtitel: Leichter leben mit der Velorin Diät – ganz einfach!
Nebentitel: Gesunde und leckere Rezepte für jede Tageszeit inkl. 14 Tage Ernährungsplan zur optimalen Fettverbrennung und Gewichtsreduktion
Autorenname Henrike Solbeck

```html
<!DOCTYPE html>
<html lang="de">
<head>
<meta charset="utf-8">
<title>Leichter leben mit der Velorin Diät – Buchcover</title>
<link href="https://fonts.googleapis.com/css2?family=Arimo:wght@400;700&family=Archivo:wght@900&display=swap" rel="stylesheet">
<style>
  :root {
    --back-pink: #ec9898;
    --front-pink: #f0a4a4;
    --front-pink-light: #f4b0ad;
    --photo-pink: #eea2a0;
    --photo-skin: #e9b7a3;
    --ink-white: #ffffff;
    --trim-line: #1a1a1a;
    --spine-guide: #3b9be0;
  }
  * { margin: 0; padding: 0; box-sizing: border-box; }
  html, body { width: 1200px; height: 597px; overflow: hidden; }
  body {
    position: relative;
    font-family: "Arimo", Arial, sans-serif;
    color: var(--ink-white);
    background: var(--back-pink);
  }
  .cover { position: absolute; inset: 0; }
  .front-panel {
    position: absolute; left: 611px; top: 0; right: 0; bottom: 0;
    background: linear-gradient(160deg, var(--front-pink) 0%, var(--front-pink-light) 45%, var(--front-pink) 100%);
  }
  .model-photo {
    position: absolute; left: 928px; top: 0; width: 272px; height: 597px;
    background: radial-gradient(ellipse 45% 60% at 60% 55%, var(--photo-skin) 0%, var(--photo-pink) 75%);
  }
  .trim-frame {
    position: absolute; left: 8px; top: 9px; width: 1182px; height: 580px;
    border: 1px solid var(--trim-line);
  }
  .spine-guide {
    position: absolute; top: 0; bottom: 0; width: 0;
    border-left: 1px dashed var(--spine-guide);
  }
  .spine-guide.left { left: 588px; }
  .spine-guide.right { left: 611px; }

  /* Back cover */
  .back-heading {
    position: absolute; left: 8px; width: 582px; top: 61px;
    text-align: center; font-weight: 700; font-size: 15px; letter-spacing: 0.1px;
  }
  .back-copy {
    position: absolute; left: 8px; width: 582px;
    text-align: center; font-size: 15.5px; line-height: 20.5px;
  }
  .back-copy.first { top: 101px; }
  .back-copy.second { top: 245px; }
  .back-copy.third { top: 367px; }

  /* Spine */
  .spine-text {
    position: absolute; left: 600px;
    font-weight: 700; font-size: 10.5px; white-space: nowrap;
    transform: translate(-50%, -50%) rotate(-90deg);
  }
  .spine-author { top: 108px; }
  .spine-title { top: 388px; }

  /* Front cover */
  .front-author {
    position: absolute; left: 648px; top: 48px;
    font-weight: 700; font-size: 14px;
  }
  .front-title {
    position: absolute; left: 648px; top: 94px;
    font-family: "Archivo", "Arial Black", sans-serif; font-weight: 900;
    font-size: 50px; line-height: 62.5px; letter-spacing: 0.5px;
  }
  .front-subtitle {
    position: absolute; left: 648px; top: 505px;
    font-weight: 700; font-size: 14px; line-height: 18.2px;
  }
</style>
</head>
<body>
<div class="cover">
  <div class="front-panel"></div>
  <div class="model-photo" role="img" aria-label="Foto einer schlanken Frau in weißer Sportunterwäsche vor rosa Hintergrund"></div>

  <h2 class="back-heading">LEICHTER LEBEN MIT DER VELORIN DIÄT - GANZ EINFACH!</h2>
  <p class="back-copy first">Odignata quatem de consedi squiate<br>nullici te dio exerum cones et et pro mo<br>corro beat ex esequia quatis adipsapelis ut pa<br>ped mo quo ipsanditis aut volent dolore ma verumquiates<br>exeribus non et odi test eosa suntur sed ma volupti<br>dolenim incilla udisquas ex etur? Alitam aut qui ommo consedi tatio.</p>
  <p class="back-copy second">Hit volorro etus estibea vitia aliquid milita perioresto inusandis<br>volores et expero con excesci lleniti tem utem quunt earum volenti<br>nctorum, nis nonseque ellatur si dero earum velitiberes dolorae pora<br>dolut es nobitaerum fugitios magnitiam sum adis elluptat.</p>
  <p class="back-copy third">Ant aliquid quat paritas aut vel il incillaccae parchit latis sam,<br>sum dunt ab idigenimet, ommolore porerio rernam aut libus et id<br>quuntem remporecti cones re none officitio il ipsunt quas venderist<br>que que ommolup itiurest lante omnimagnimo quiderem illabore<br>naturit et occusandita inctis dollupt atemodionse que cum que<br>volore volupti aspite erae.</p>

  <div class="spine-text spine-author">HENRIKE SOLBECK</div>
  <div class="spine-text spine-title">LEICHTER LEBEN MIT DER VELORIN DIÄT – GANZ EINFACH!</div>

  <div class="front-author">HENRIKE SOLBECK</div>
  <h1 class="front-title">LEICHTER<br>LEBEN MIT<br>DER VELORIN<br>DIÄT –<br>GANZ<br>EINFACH!</h1>
  <p class="front-subtitle">GESUNDE UND LECKERE REZEPTE FÜR JEDE TAGESZEIT<br>INKL. 14 TAGE ERNÄHRUNGSPLAN ZUR OPTIMALEN<br>FETTVERBRENNUNG UND GEWICHTSREDUKTION</p>

  <div class="spine-guide left"></div>
  <div class="spine-guide right"></div>
  <div class="trim-frame"></div>
</div>
</body>
</html>
```